Flyer Design Project

Brindlewick is an IT support company based in the UKl . We protect small busineses from online criminals, malware threats, and technology failure. We do this by creating layers of protection around our clients and their business. We show them the dangers they’re exposed to and how we’ll eliminate them.

We would like to market some special promotions for our managed it services. We want a double sided leaflet , One side will focus on sign up today and get 2 months free it support. On the other we would want to talk about we will not be beaten on price, we offer pro active IT support. Content would need to be along those lines.

I have added a brochure that we have used in the past. Use for ideas.

Industry/Entity Type

Business

```html
<!DOCTYPE html>
<html lang="en">
<head>
<meta charset="utf-8">
<title>Brindlewick – Managed IT Support Leaflet (Back)</title>
<link href="https://fonts.googleapis.com/css2?family=Fira+Sans:ital,wght@0,500;1,400;1,800&family=Tinos:wght@400;700&display=swap" rel="stylesheet">
<style>
  :root{
    --page:#e4e5e6;
    --paper:#ffffff;
    --panel:#1b98d5;
    --panel-light:#2aa6e0;
    --ink:#2f3133;
    --accent:#1f7fc4;
    --white:#ffffff;
    --partner-mark:#9aa3a9;
    --photo-dark:#0e2438;
    --photo-mid:#2d6f99;
  }
  *{box-sizing:border-box;margin:0;padding:0}
  html,body{width:1200px;height:888px;overflow:hidden;background:var(--page)}
  .leaflet{
    position:absolute;left:300px;top:20px;width:600px;height:848px;
    background:var(--paper);box-shadow:0 0 0 1px #d2d4d6;
    font-family:"Tinos","Times New Roman",serif;
  }
  .hero-photo{
    position:absolute;left:14px;top:2px;width:148px;height:225px;
    border-radius:0 0 14px 14px;
    background:radial-gradient(circle at 55% 35%,var(--photo-mid),var(--photo-dark) 75%);
  }
  .partners-title{
    position:absolute;left:0;top:242px;width:176px;text-align:center;
    font-family:"Fira Sans",sans-serif;font-style:italic;font-weight:800;
    font-size:19px;color:var(--accent);
  }
  .partner-list{position:absolute;left:0;top:270px;width:176px;list-style:none}
  .partner{
    height:83px;display:flex;align-items:center;justify-content:center;gap:7px;
    font-family:"Fira Sans",sans-serif;font-weight:500;font-size:16px;color:var(--ink);
  }
  .partner-dot{width:12px;height:12px;border-radius:50%;background:var(--partner-mark)}
  .info-panel{
    position:absolute;left:174px;top:0;width:434px;height:762px;
    background:linear-gradient(180deg,var(--panel-light),var(--panel));
    color:var(--white);
  }
  .topic{position:absolute;left:14px;width:392px}
  .topic h2{font-weight:400;font-size:19px;margin-bottom:7px}
  .topic p{font-size:11.4px;line-height:14.6px;margin-bottom:5px}
  .topic.lead h2{font-size:23px;margin-bottom:6px}
  .topic.lead p{font-size:13.6px;line-height:16.2px;font-weight:700;margin-bottom:6px}
  .promise{
    position:absolute;left:14px;top:694px;width:410px;
    font-family:"Fira Sans",sans-serif;font-style:italic;font-weight:800;
    font-size:24px;line-height:30px;
  }
  .call-to-action{
    position:absolute;left:174px;top:768px;width:434px;text-align:center;
    font-family:"Fira Sans",sans-serif;font-style:italic;font-weight:400;
    font-size:21px;line-height:26px;color:var(--ink);
  }
</style>
</head>
<body>
  <main class="leaflet">
    <div class="hero-photo" role="img" aria-label="Photo of a businessman's hand touching a glowing cloud icon on a dark blue background"></div>

    <h3 class="partners-title">Our Partners:</h3>
    <ul class="partner-list">
      <li class="partner"><span class="partner-dot"></span>Orchardline</li>
      <li class="partner">Searchwell Apps</li>
      <li class="partner">Relaymail</li>
      <li class="partner">Talkwave</li>
      <li class="partner">Hostrack</li>
      <li class="partner">Chatterdesk</li>
      <li class="partner">Airlink</li>
    </ul>

    <section class="info-panel">
      <article class="topic" style="top:20px">
        <h2>How does “average” IT support usually work?</h2>
        <p>Average IT support is reactive. Something bad happens and you call your IT guys in a panic. You’ve lost your backups, a virus prevents your team from working, or something’s not working right.</p>
        <p>Reactive IT support means you’ll always have downtime, and you’ll always lose money every time something goes wrong. You lose money while you wait for viruses to be cleaned, backups to be restored, maintenance to be completed, or updates to be made.</p>
      </article>

      <article class="topic" style="top:188px">
        <h2>What is doting IT support?</h2>
        <p>Doting IT support is proactive. Our managed IT service means we don’t wait for you to realise there’s a problem; we monitor the computers and devices in your network, in real time. We look for threats to your business, areas that need improvement, and ways to improve performance. We find and fix IT problems immediately and automatically, minimising downtime or eliminating it all together. Now that rootkit your employee uploaded after work on Friday doesn’t stop you from working on Monday.</p>
      </article>

      <article class="topic" style="top:358px">
        <h2>You’ll still have to deal with the unexpected.</h2>
        <p>That’s right. Remember though, that your downtime skyrockets when your IT support receives secondhand information.</p>
        <p>Our managed IT subscription means that we find and fix IT problems automatically. Since we already know what the problem is there’s no need for you to explain anything and we don’t spend time getting usernames and passwords from you.</p>
      </article>

      <article class="topic lead" style="top:514px">
        <h2>Why do I need doting IT support?</h2>
        <p>You need it because you don’t know what you don’t know. Can you spot employee bad habits that expose your business to theft? Can you find and fix security holes that make your private information public?</p>
        <p>Not without support. Sign up today for 2 months free – we won’t be beaten on price.</p>
      </article>

      <p class="promise">Reduce downtime and expenses<br>by as much as 93%.</p>
    </section>

    <p class="call-to-action">Call Brindlewick on<br>0871 555 0142<br>to schedule your free IT audit.</p>
  </main>
</body>
</html>
```